Corvelle Strategies business card

I need a business card for my new strategic consulting LLC, Corvelle Strategies. We specialize in helping people who care about broadband technology and telecommunications policy, and we're based in Washington DC. I'm looking for a card that says smart, credible, future-facing and signals a high level of expertise. It's DC, so there's clearly a limit to how crazy we can go with this card, but I am looking for a design that reflects a company that is comfortable with technology, policy, and having a little bit fun. I'm uploading my logo below, and I'd like to have it be part of the card design in some fashion.
Target Market(s)
Telecommunications and technology policy professionals
Industry/Entity Type
Technology policy
Contact Information for Business Card
Name of business, my name (Glen Mosswater), email (glen@corvellestrategies-example.com) , phone number (202-555-0148)phone number

```html
<!DOCTYPE html>
<html lang="en">
<head>
<meta charset="utf-8">
<title>Corvelle Strategies – Business Card</title>
<link href="https://fonts.googleapis.com/css2?family=Montserrat:wght@500;600;700&family=Nunito+Sans:wght@400&display=swap" rel="stylesheet">
<style>
  :root {
    --brand-blue: #0a539c;
    --accent-orange: #f29a22;
    --paper: #ffffff;
    --mist: #d9dae0;
    --stage: #eef0f3;
    --text-blue: #0d4a8c;
  }
  * { margin: 0; padding: 0; box-sizing: border-box; }
  html, body { width: 1200px; height: 900px; overflow: hidden; }
  body {
    background: var(--stage);
    display: flex;
    align-items: center;
    justify-content: center;
    gap: 30px;
    font-family: "Montserrat", sans-serif;
  }
  .card {
    position: relative;
    width: 560px;
    height: 336px;
    background: var(--paper);
    overflow: hidden;
    box-shadow: 4px 5px 10px rgba(0,0,0,0.28);
  }

  /* Front */
  .front-band {
    position: absolute; left: 0; top: 0; bottom: 0; width: 47px;
    background: var(--brand-blue);
  }
  .front-accent {
    position: absolute; left: 44px; bottom: 0; width: 6px; height: 98px;
    background: var(--accent-orange);
  }
  .skyline {
    position: absolute; right: 0; bottom: 0; width: 330px; height: 200px;
    background:
      linear-gradient(to right, rgba(255,255,255,1) 0%, rgba(255,255,255,0) 45%),
      linear-gradient(to bottom, rgba(255,255,255,0) 0%, var(--mist) 55%, var(--mist) 100%);
  }
  .wordmark {
    display: flex; align-items: center; gap: 8px;
    font-weight: 700; letter-spacing: -0.5px;
    white-space: nowrap;
  }
  .wordmark .dot {
    width: 14px; height: 14px; border-radius: 50%;
    background: var(--accent-orange); flex: none;
  }
  .front .wordmark {
    position: absolute; left: 80px; top: 112px;
    font-size: 30px; color: var(--brand-blue);
  }
  .tagline {
    position: absolute; left: 80px; width: 310px; top: 186px;
    text-align: center;
    font-size: 8.5px; font-weight: 600; letter-spacing: 1.1px;
    color: var(--text-blue);
  }

  /* Back */
  .back-panel { position: absolute; inset: 0; }
  .back .wordmark {
    position: absolute; left: 26px; top: 150px;
    color: var(--paper); font-size: 22px;
  }
  .person {
    position: absolute; left: 326px; top: 72px;
  }
  .person-name {
    font-size: 20px; font-weight: 500; color: var(--text-blue);
    letter-spacing: 0.4px; white-space: nowrap;
  }
  .person-rule {
    width: 78px; height: 2px; background: var(--accent-orange);
    margin: 3px 0 0 5px;
  }
  .person-role {
    font-size: 10px; font-weight: 500; letter-spacing: 0.6px;
    color: var(--text-blue); margin: 5px 0 0 5px;
  }
  .contacts {
    position: absolute; left: 326px; top: 144px;
    list-style: none;
    font-family: "Nunito Sans", sans-serif;
    font-size: 10.5px; color: var(--text-blue);
  }
  .contacts li {
    display: flex; align-items: center; height: 20px; margin-bottom: 23px;
    white-space: nowrap;
  }
  .contacts svg { width: 14px; height: 14px; margin-right: 12px; flex: none; }
</style>
</head>
<body>

  <section class="card front" aria-label="Card front">
    <div class="front-band"></div>
    <div class="front-accent"></div>
    <div class="skyline" role="img" aria-label="Faint grey city skyline with light streaks"></div>
    <div class="wordmark"><span>Corvelle Strategies</span><span class="dot"></span></div>
    <p class="tagline">INSIGHT.POLICY.BROADBAND</p>
  </section>

  <section class="card back" aria-label="Card back">
    <svg class="back-panel" width="560" height="336" viewBox="0 0 560 336" aria-hidden="true">
      <polygon points="0,0 319,0 239,336 0,336" fill="var(--brand-blue)"/>
      <polygon points="261,243 267,243 245,336 239,336" fill="var(--accent-orange)"/>
    </svg>
    <div class="wordmark"><span>Corvelle Strategies</span><span class="dot"></span></div>

    <div class="person">
      <p class="person-name">Glen Mosswater</p>
      <div class="person-rule"></div>
      <p class="person-role">PRINCIPAL</p>
    </div>

    <ul class="contacts">
      <li>
        <svg viewBox="0 0 24 24" aria-hidden="true"><path fill="var(--text-blue)" d="M6.6 10.8a15.1 15.1 0 0 0 6.6 6.6l2.2-2.2c.3-.3.7-.4 1-.2 1.1.4 2.3.6 3.6.6.6 0 1 .4 1 1V20c0 .6-.4 1-1 1A17 17 0 0 1 3 4c0-.6.4-1 1-1h3.5c.6 0 1 .4 1 1 0 1.3.2 2.5.6 3.6.1.3 0 .7-.2 1z"/></svg>
        (202-555-0148)
      </li>
      <li>
        <svg viewBox="0 0 24 24" aria-hidden="true"><rect x="2" y="5" width="20" height="14" rx="1.5" fill="var(--text-blue)"/><path d="M3 6.5l9 6.5 9-6.5" fill="none" stroke="#fff" stroke-width="1.4"/></svg>
        glen@corvellestrategies-example.com
      </li>
      <li>
        <svg viewBox="0 0 24 24" aria-hidden="true" fill="none" stroke="var(--text-blue)" stroke-width="1.6"><circle cx="12" cy="12" r="9.5"/><ellipse cx="12" cy="12" rx="4.2" ry="9.5"/><path d="M2.5 12h19M4 7h16M4 17h16"/></svg>
        corvellestrategies-example.com
      </li>
      <li>
        <svg viewBox="0 0 24 24" aria-hidden="true"><path fill="var(--text-blue)" d="M12 2a7 7 0 0 0-7 7c0 5.2 7 13 7 13s7-7.8 7-13a7 7 0 0 0-7-7zm0 9.5A2.5 2.5 0 1 1 12 6.5a2.5 2.5 0 0 1 0 5z"/></svg>
        Washington, D.C.
      </li>
    </ul>
  </section>

</body>
</html>
```